Berichtslayout für Unternehmensberatung mit Schwerpunkt Softwareentwicklung für den Public Sektor
Wir sind eine Unternehmensberatung, die sich auf Softwareentwicklung für den Public Sektor spezialisiert hat (www.tqm-beratung.de). Unsere Zielgruppe sind Verwaltungen im deutschsprachigen Raum. Wir bieten für diesen Markt verschiedene Softwareprodukte an. Aus unseren Softwareprodukten werden automatische Controllingberichte erzeugt.
Company
We are a consulting company, that is specialised in softwaredevelopment regarding the public sector (www.tqm-beratung.de). Our customers are administrations all over Germany, Austria and Swiss. We offer different products to the market. One of which produces a report you can find enclosed to this project.
Aufgabenstellung
Es soll ein Berichtslayout erstellt werden.
• Das Berichtslayout muss die Informationen des Berichtsentwurfs aufnehmen können, beispielsweise Tabellen etc. (Anlage 1)
• Der Bericht enthält viel Text und viele Zahlen, weshalb auch ein Vorschlag über die Gestaltung der Tabellen enthalten sein soll. (Anlage 1)
• Das Layout kann Symbole wie den Falkmoorer Zeichen oder die Farben des Deckblatts aufnehmen (Anlage 2). Alle anderen Elemente können verändert werden.
• Schriftart muss Calibri sein.
• Das Berichtslayout soll übersichtlich und ansprechend aussehen.
• Das Berichtslayout soll, soweit möglich, nicht überladen wirken.
Der Bericht wird über jasper Reports erzeugt.
Wenn das Design in AI oder Indesign entwickelt wird, sollten wir dies verwenden können.
Task:
We need a better Layout for our report.
• The Layout has to be able to handle the informations shown in 'Anlage 1'.
• The layout can use Symbols like the 'Falkmoorer Zeichen' (Falkmoorer Sign) or colors of the covering page shown in 'Anlage 2'.
• Since the Layout has to handle a lot of numbers an text it would be nice if you could deliver a layout suggestion for those elements as well
• The Font has to be Calibri
• The Layout sould look as clean and appealing as possible.

```html
<!DOCTYPE html>
<html lang="de">
<head>
<meta charset="utf-8">
<title>Controllingbericht Produktgruppenhaushalt – Layout</title>
<link href="https://fonts.googleapis.com/css2?family=Carlito:wght@400;700&family=Open+Sans:wght@400;600;700&display=swap" rel="stylesheet">
<style>
  :root{
    --red:#d90a1e;
    --ink:#3a3a3a;
    --muted:#6b6b6b;
    --paper:#ffffff;
    --stage:#f3f3f3;
    --rule:#c9c9c9;
    --row:#ececec;
  }
  *{box-sizing:border-box;margin:0;padding:0}
  html,body{width:1200px;height:3024px;overflow:hidden;background:var(--stage)}
  body{position:relative;font-family:'Carlito',Calibri,sans-serif;color:var(--ink)}
  .page{position:absolute;width:483px;height:683px;background:var(--paper);box-shadow:0 4px 14px rgba(0,0,0,.22);overflow:hidden}

  /* cover */
  .cover{left:330px;top:108px;width:482px}
  .cover-photo{position:absolute;inset:0;background:linear-gradient(160deg,#9a9a9c 0%,#5d5e62 35%,#3b3c40 65%,#6e6f72 100%)}
  .cover-panel{position:absolute;left:0;top:95px;width:354px;height:501px;background:var(--red);color:#fff}
  .brand{position:absolute;left:29px;top:28px;font-family:'Open Sans',sans-serif;font-weight:700;font-size:14px;letter-spacing:.2px}
  .brand-name{font-size:24px;margin-right:8px}
  .cover-title{position:absolute;left:29px;top:188px;font-family:'Open Sans',sans-serif;font-weight:600;font-size:24.5px;line-height:35px}
  .cover-period{position:absolute;left:29px;top:268px;font-family:'Open Sans',sans-serif;font-size:16px}
  .cover-rule{position:absolute;left:29px;top:436px;width:293px;height:1px;background:#fff}
  .issuer{position:absolute;left:29px;top:466px;font-family:'Open Sans',sans-serif;font-size:15px;display:flex;align-items:center;gap:22px}
  .issuer-mark{width:18px;height:18px;border:2px solid #fff}

  /* contents */
  .contents-photo{position:absolute;left:0;top:0;width:241px;height:683px;background:linear-gradient(180deg,#3a3d44 0%,#8e9097 18%,#e9e4df 40%,#c9a487 55%,#d8d4d0 75%,#9fa1a6 100%)}
  .contents-bar{position:absolute;left:0;top:151px;width:398px;height:57px;background:var(--red);color:#fff;font-family:'Open Sans',sans-serif;font-weight:600;font-size:25px;letter-spacing:2px;text-align:right;padding-right:27px;line-height:57px}
  .toc{position:absolute;left:272px;top:250px;list-style:none}
  .toc li{display:flex;gap:12px;margin-bottom:20px}
  .toc-num{font-family:'Open Sans',sans-serif;color:var(--red);font-size:26px;line-height:30px;width:40px}
  .toc-title{font-family:'Open Sans',sans-serif;font-weight:700;font-size:13px;line-height:15px;padding-top:5px}
  .toc-sub{font-size:11px;color:var(--muted);font-weight:400;font-family:'Carlito',sans-serif}

  /* summary */
  .summary-box{position:absolute;left:128px;top:88px;width:355px;height:502px;background:var(--red);color:#fff;font-family:'Open Sans',sans-serif}
  .summary-title{position:absolute;top:94px;width:100%;text-align:center;font-weight:700;font-size:26px;line-height:35px}
  .facts{position:absolute;left:45px;top:220px;font-size:13px;line-height:17px}
  .fact{display:grid;grid-template-columns:117px 1fr;margin-bottom:12px}
  .fact-val{font-weight:700}
  .fact-val span{display:inline-block;width:40px}
  .mark{font-size:12px}

  /* text pages */
  .tab{position:absolute;left:0;top:29px;height:30px;background:var(--red);color:#fff;font-family:'Open Sans',sans-serif;font-weight:700;font-size:13px;letter-spacing:.5px;padding:0 29px;line-height:30px}
  .tab.tall{top:32px;height:55px;line-height:20px;padding-top:8px;width:250px}
  .body{position:absolute;left:29px;right:29px;font-size:7.4px;line-height:10.2px;color:#333}
  .body h3{font-family:'Open Sans',sans-serif;font-weight:700;font-size:9.5px;color:#444;margin:0 0 14px;text-transform:uppercase;display:inline-block;border-bottom:1px solid #444;padding-bottom:1px}
  .body h4{color:var(--red);font-weight:400;font-size:7.6px;margin-top:8px}
  .body p{margin-bottom:8px;text-align:justify}
  .footer{position:absolute;left:29px;right:29px;bottom:0;height:30px;font-size:7.6px;color:#555}
  .footer .l{position:absolute;left:0;top:6px;line-height:9px}
  .footer .r{position:absolute;right:0;top:10px;line-height:9px;text-align:right}
  .footer .pn{position:absolute;left:194px;top:0;width:39px;height:30px;background:var(--red);color:#fff;text-align:center;line-height:30px;font-size:8px}

  .measures{position:absolute;left:29px;right:29px;top:118px;list-style:none;font-size:7.3px;line-height:9.6px}
  .measures li{display:flex;gap:3px;margin-bottom:5px}
  .measures b{color:var(--red);font-weight:400}

  table{border-collapse:collapse;font-size:5px;line-height:7px;width:100%}
  .budget{position:absolute;left:29px;top:274px;width:428px;border:1px solid #888}
  .budget td,.budget th{padding:1px 2px;text-align:right;white-space:nowrap}
  .budget th{color:var(--red);font-weight:400;font-size:4.6px}
  .budget .corner{background:var(--red);color:#fff;font-weight:700;font-size:6.4px;text-align:center;line-height:9px}
  .budget td:first-child{text-align:left}
  .budget .sum td{font-weight:700;border-top:1px solid #999;border-bottom:1px solid #999}
  .budget .saldo td{font-weight:700;background:var(--row);border-top:1px solid #666}
  .budget .grp{border-left:1px solid #bbb}
  .sub-h{position:absolute;left:29px;font-family:'Open Sans',sans-serif;font-weight:700;font-size:9.5px;color:#444;border-bottom:1px solid #444;padding-bottom:1px}
  .legend{position:absolute;left:29px;top:530px;font-size:7.2px;line-height:15px;display:grid;grid-template-columns:75px 115px 145px 1fr}
  .legend span{display:flex;align-items:center;gap:4px}
  .dot{width:8px;height:8px;border-radius:50%;display:inline-block}
  .goals{position:absolute;left:29px;top:573px;width:408px;border:1px solid #888}
  .goals td,.goals th{padding:1px 2px;text-align:right}
  .goals th{color:var(--red);font-weight:400;font-size:4.6px}
  .goals .corner{background:var(--red);color:#fff;font-weight:700;font-size:6px;text-align:center}
  .goals td:first-child{text-align:left}
</style>
</head>
<body>

<!-- Cover -->
<section class="page cover">
  <div class="cover-photo" role="img" aria-label="Luftaufnahme einer Großstadt mit Hochhäusern in Grautönen"></div>
  <div class="cover-panel">
    <div class="brand"><span class="brand-name">tqm</span>tanner, quast &amp; meinert</div>
    <h1 class="cover-title">Controllingbericht<br>Produktgruppenhaushalt</h1>
    <div class="cover-period">Januar - Juni 2019</div>
    <div class="cover-rule"></div>
    <div class="issuer"><span class="issuer-mark"></span>Die Finanzbehörde Falkmoor</div>
  </div>
</section>

<!-- Contents -->
<section class="page" style="left:107px;top:824px">
  <div class="contents-photo" role="img" aria-label="Foto eines Händedrucks zweier Geschäftsleute"></div>
  <div class="contents-bar">INHALT</div>
  <ul class="toc">
    <li><span class="toc-num">39</span><div class="toc-title">Kommentar<div class="toc-sub">Lorem Ipsum</div></div></li>
    <li><span class="toc-num">41</span><div class="toc-title">Maßnahmen-<br>Steuerungsvorschlag<div class="toc-sub">Lorem Ipsum</div></div></li>
    <li><span class="toc-num">47</span><div class="toc-title">Dolor sit Amet<div class="toc-sub">Lorem Ipsum</div></div></li>
    <li><span class="toc-num">55</span><div class="toc-title">Dolor sit Amet<div class="toc-sub">Lorem Ipsum</div></div></li>
    <li><span class="toc-num">70</span><div class="toc-title">Dolor sit Amet<div class="toc-sub">Lorem Ipsum</div></div></li>
  </ul>
</section>

<!-- Summary -->
<section class="page" style="left:612px;top:824px">
  <div class="summary-box">
    <h2 class="summary-title">Controlling 01-06/19<br>28.09.19</h2>
    <div class="facts">
      <div class="fact" style="margin-bottom:30px"><div>Produktplan<br>Verantwortlich</div><div class="fact-val">07 Inneres<br>Senator Kötterling</div></div>
      <div class="fact"><div>Einhaltung<br>Finanzdaten</div><div class="fact-val"><span>Land</span><b class="mark">✕</b><br><span>Stadt</span><b class="mark">✕</b></div></div>
      <div class="fact"><div>Einhaltung<br>Personaldaten</div><div class="fact-val"><span>Land</span><b class="mark">✕</b><br><span>Stadt</span><b class="mark">✓</b></div></div>
      <div class="fact"><div>Einhaltung<br>strategische Ziele</div><div class="fact-val"><span>Land</span><b class="mark">✓</b><br><span>Stadt</span><b class="mark">✓</b></div></div>
    </div>
  </div>
</section>

<!-- Page 39 -->
<section class="page" style="left:107px;top:1526px">
  <div class="tab">KOMMENTAR</div>
  <div class="body" style="top:82px">
    <h3>Finanzdaten</h3>
    <h4>PPL 07</h4>
    <p>Der PPL 07 wird sein Budget nach gegenwärtigem Stand um 12,8 Mio. € überschreiten (Land: 5,9 Mio. €; Stadt: 6,9 Mio. €). Im Vergleich zum Controlling 01-05/2019 ergibt sich damit eine Verschlechterung in Höhe von 4,5 Mio. €. Die Verschlechterung setzt sich aus folgenden Veränderungen zusammen:<br>Erhöhung Mindereinnahmen um 2 Mio. € (Land: 1,7 + Stadt: 0,3)<br>Reduzierung Personalmehrausgaben um 2 Mio. € (Land: -1,8; Stadt: -0,2)<br>Erhöhung konsumtive Mehrausgaben um 3,2 Mio. € (Stadt: 3,2)<br>Erhöhung investive Mehrausgaben um 1,3 Mio. € (Stadt: 1,3)</p>
    <h4>Konsumtive Einnahmen</h4>
    <p>Bei den konsumtiven Einnahmen werden derzeit rd. 2,2 Mio. € an Mindereinnahmen prognostiziert. Die Verschlechterung um ca. 2 Mio. € im Vergleich zum letzten Controlling entsteht insbesondere dadurch, dass die noch im Controlling 01-05/2019 ausgewiesenen Mehreinnahmen für Polizeieinsätze bei Hochrisiko-Fußballspielen von 1,5 Mio. € auf 1,2 Mio. € abgesenkt wurden. Im Controlling 01-04 ging man noch von Einnahmen in Höhe von 2 Mio. € aus. Des Weiteren sollen laut Ressort vorbehaltlich einer entsprechenden Gremienbefassung die voraussichtlichen Einnahmen komplett für die Auszahlung von Überstunden bei der Polizei verwendet werden. Folglich wären sie dadurch nicht mehr als Mehreinnahmen vorhanden. Im Controlling 01-05 sollten dagegen bisher nur lediglich 0,5 Mio. € dafür verwendet werden. Es bleibt zudem abzuwarten, ob die Einnahmen überhaupt noch in 2019 eingehen.</p>
    <p>Des Weiteren haben sich die Mindereinnahmen bei den Gebühren für Feuerwehreinsätze um 0,4 Mio. € erhöht und es entstehen Mindereinnahmen in der Produktgruppe Wahlen in Höhe von 0,2 Mio. €. Laut Ressort wird die Kostenerstattung zur Wahl des europäischen Parlaments geringer ausfallen, da aufgrund der gleichzeitig durchgeführten Wahlen nicht alle Kosten abrechnungsfähig sind. In den Produktgruppen im Bereich „Öffentliche Ordnung“ haben sich die Mindereinnahmen geringfügig von 0,262 Mio. € auf 0,17 Mio. € reduziert.</p>
    <h4>Konsumtive Ausgaben</h4>
    <p>Bei den konsumtiven Ausgaben werden zum Jahresende derzeit 3,7 Mio. € an Mehrausgaben prognostiziert. Die Steigerung der Ausgaben im Vergleich zum Controlling 01-05/2019 i. H. v. 3,2 Mio. € ergibt sich insbesondere durch Mehrausgaben im Rettungsdienst. Laut Ressort liegt dies zum Großteil an den aus der Monatsabrechnung losgelösten Auszahlungen an Hilfsorganisationen. Des Weiteren stehen für den Bereich Notärzte noch Rechnungen aus.</p>
    <p>Zusätzlich zu den durch das beschlossene Kapazitätskonzept II entstehenden Bedarfen für die zusätzliche Einstellung von Studierenden im Polizeivollzug prognostiziert die Polizei zusätzliche Mehrausgaben i. H. v. 1,2 Mio. € für Geschäftsbedarf und Digitalfunkgeräte (0,57 Mio. €), DNA- und BTM Fremdvergabe (0,270 Mio. €) sowie Dolmetscherkosten (0,145 Mio. €). Diese Mehrbedarfe wurden im letzten Controlling 01-05/2019 nicht ausgewiesen.</p>
    <p>Dem gegenüber stehen dagegen konsumtive Minderausgaben im Umfang von 1,2 Mio. € aufgrund geringerer Ausgaben für die Bürgerschafts- und Beiratswahl sowie der Europawahl. Insbesondere die Druckkosten sind laut Ressort erheblich niedriger ausgefallen, als ursprünglich vom Ressort erwartet.</p>
  </div>
  <footer class="footer"><div class="l">Controlling 01-06/19<br>28.09.19</div><div class="pn">39</div><div class="r">07 Inneres</div></footer>
</section>

<!-- Page 40 -->
<section class="page" style="left:612px;top:1526px">
  <div class="body" style="top:28px">
    <h4 style="margin-top:0">Investive Ausgaben</h4>
    <p>Bei den investiven Ausgaben werden Mehrausgaben im Umfang von 3,866 Mio. € prognostiziert. Im Vergleich zum letzten Controlling ergibt sich damit eine Verschlechterung i. H. v. rd. 1,3 Mio. €. Die Verschlechterung tritt ausschließlich im Rettungsdienst auf und ist darauf zurückzuführen, dass die Rettungsdienst-Fahrzeuge nicht mehr über den Nordhilfe Rettungsverbund beschafft und finanziert werden, sondern über den Haushalt beschafft werden. In der Gebührenkalkulation wird zudem nur rd. ein Fünftel des Betrages an Abschreibungen aufgenommen.</p>
    <p>Vor dem Hintergrund der dadurch entstehenden finanziellen Auswirkungen wird die Innenbehörde in Abstimmung mit der Finanzbehörde eine vertiefte Betrachtung der Entwicklung der investiven Ausgaben des Rettungsdienstes vornehmen. Dies beinhaltet die konkreten Planungen zur Fahrzeugbeschaffung sowie Berücksichtigung in der Gebührenkalkulation.</p>
    <p>Des Weiteren fallen laut Ressort für das Projekt Mobile Datenerfassung rd. 2 Mio. € an Ausgaben an. Hier sollte seitens des Innenressorts geprüft werden, in wie weit diese Kosten im Rahmen der Gebührenkalkulation eingeflossen sind. Insgesamt entstehen damit in der Produktgruppe Rettungsdienst Mehrausgaben i. H. v. 1,8 Mio. €.</p>
    <h4>Finanzierungssaldo</h4>
    <p>Der zulässige produktplanbezogene Finanzierungssaldo wird unter Berücksichtigung von produktplanübergreifenden Verlagerungen (ca. 25,6 Mio. €) um rd. 14,454 Mio. € (Land: 7,3 Mio. €; Stadt: 7,1 Mio. €) überschritten. Die Differenz zwischen der Budgetüberschreitung (12,8 Mio. €) und der Überschreitung des Finanzierungssaldos lässt sich teilweise durch die aus 2018 übertragenen haushaltsmäßig nicht finanzierten Rücklagen erklären.</p>
    <h3 style="margin-top:26px">Personaldaten</h3>
    <p>Im Produktplan 07 – Inneres – werden voraussichtliche Personalmehrausgaben in Höhe von rund 3,5 Mio. € erwartet. Dies korrespondiert mit einer vom Ressort geplanten erheblichen Überschreitung der Zielzahlen und Sollvorgaben zum Jahresende. Die Mehrausgaben und Überschreitungen fallen ausschließlich im Land an und resultieren größtenteils aus geplanten bzw. bereits vollzogenen Neueinstellungen sowie auf umfangreiche Beförderungen in den letzten Jahren (Überschreitung Land: ca. 3,65 Mio. €, Unterschreitung Stadt: ca. 0,15 Mio. €).</p>
    <p>Gegenüber den Vormonaten weist der Produktplan 07 eine Verbesserung um rund 1,7 Mio. € aus. Ursächlich für die Differenz war eine doppelte Berücksichtigung von zukünftigen Personaleinstellungen in der Ressortprognose. Dabei wurden u.a. folgende Sollveränderungen berücksichtigt: erwartete Nachbewilligungen bzw. Einsparungen für die Durchführung der Wahlen 2019, für die Aussteuerung der Ausbildungsplanung sowie zentrale Ausgleiche der Beihilfen und Nachversicherungen.</p>
    <p>Auf der Ausgabeseite wurden u.a. folgende Punkte im voraussichtlichen Ist berücksichtigt: erwartete Personalausgaben aufgrund von Neueinstellungen im Kernbereich und bei den temporären Personalmitteln bzw. in den Handlungsfeldern, aufgrund von Übernahmen aus der Ausbildung bei der Polizei und bei der Feuerwehr sowie die erwartete Restfluktuation.</p>
    <p>Eine mögliche Problemlösung wird von Innenressort nicht aufgezeigt. Es ist ein restriktives personalwirtschaftliches Handeln erforderlich.</p>
  </div>
  <footer class="footer"><div class="l" style="top:10px">07 Inneres</div><div class="pn" style="left:221px">40</div><div class="r" style="top:6px">Controlling 01-06/19<br>28.09.19</div></footer>
</section>

<!-- Page 41 -->
<section class="page" style="left:107px;top:2233px">
  <div class="tab tall">MASSNAHMEN-<br>STEUERUNGSVORSCHLAG</div>
  <ol class="measures">
    <li><b>1</b><span>Das Ressort wird gebeten, die Höhe der Bedarfe aus den Kapazitätskonzepten I und II zu überprüfen und entsprechend des Beschlusses des Senats vom 30. April 2019 zunächst eine Lösung innerhalb des Produktplanbudgets sicherzustellen.</span></li>
    <li><b>2</b><span>Das Ressort wird gebeten, im Controlling 01-09/2019 die konsumtiven Mehrbedarfe der Polizei, ggfs. durch Mengengerüste, detaillierter darzustellen und zu erläutern, weshalb diese Bedarfe erstmalig im Controlling 01-06/2019 dargestellt wurden.</span></li>
    <li><b>3</b><span>Das Ressort wird gebeten, sämtliche Möglichkeiten zur Verbesserung der Einnahmen und zur Reduzierung der Ausgaben zu ergreifen um die Höhe der erwarteten Budgetrisiken zum Jahresende noch zu minimieren.</span></li>
  </ol>
  <div class="sub-h" style="top:247px">RESSOURCENEINSATZ</div>
  <table class="budget">
    <tr><th rowspan="3" class="corner">Kamerale<br>Finanzdaten</th><th colspan="5" style="text-align:center;font-weight:700">Januar - Juni 2019</th><th colspan="4" class="grp" style="text-align:center;font-weight:700">Jahresplanung 2019</th></tr>
    <tr><th>Ist</th><th>Planwert</th><th>Ist-Planwert Abw.</th><th>%</th><th>HH-Soll</th><th class="grp">vor. HH-Soll</th><th>vor. Ist</th><th>Abweichung</th><th>Anschlag</th></tr>
    <tr><th colspan="3" style="text-align:center;color:#555">Tsd. EUR</th><th>%</th><th></th><th colspan="4" class="grp" style="text-align:center;color:#555">Tsd. EUR</th></tr>
    <tr><td>Konsumtive Einnahmen</td><td>28.725</td><td>31.545</td><td>-2.819</td><td>-8,94</td><td>53.854</td><td class="grp">59.965</td><td>57.789</td><td>-2.176</td><td>58.126</td></tr>
    <tr><td>Investive Einnahmen</td><td>36</td><td>19</td><td>17</td><td>86,62</td><td>49</td><td class="grp">49</td><td>84</td><td>35</td><td>48</td></tr>
    <tr><td>Verrechnungen/Erstattungen (Einn)</td><td>6.333</td><td>5.577</td><td>755</td><td>13,54</td><td>9.255</td><td class="grp">9.318</td><td>9.318</td><td>0</td><td>9.313</td></tr>
    <tr><td>&nbsp;- Land, Stadtgem. u. intern</td><td>6.332</td><td>5.577</td><td>755</td><td>13,53</td><td>9.253</td><td class="grp">9.254</td><td>9.254</td><td>0</td><td>9.248</td></tr>
    <tr><td>&nbsp;- von Nordhafen</td><td>1</td><td>0</td><td>1</td><td></td><td>2</td><td class="grp">64</td><td>64</td><td>0</td><td>64</td></tr>
    <tr class="sum"><td>Budgetierte Einnahmen</td><td>35.094</td><td>37.142</td><td>-2.047</td><td>-5,51</td><td>63.158</td><td class="grp">69.332</td><td>67.191</td><td>-2.141</td><td>67.487</td></tr>
    <tr><td>Personalausgaben</td><td>99.179</td><td>89.774</td><td>9.405</td><td>10,48</td><td>199.715</td><td class="grp">205.249</td><td>208.332</td><td>3.083</td><td>183.805</td></tr>
    <tr><td>Zinsausgaben</td><td>0</td><td>11</td><td>-11</td><td>-100,0</td><td>23</td><td class="grp">23</td><td>23</td><td>0</td><td>34</td></tr>
    <tr class="sum"><td>Budgetierte Ausgaben</td><td>166.008</td><td>156.339</td><td>9.669</td><td>6,18</td><td>322.361</td><td class="grp">330.588</td><td>341.254</td><td>10.666</td><td>301.484</td></tr>
    <tr class="saldo"><td>SALDO</td><td>-130.914</td><td>-119.197</td><td>-11.716</td><td>-9,83</td><td>-259.203</td><td class="grp">-261.256</td><td>-274.063</td><td>-12.807</td><td>-233.997</td></tr>
  </table>
  <div class="sub-h" style="top:498px">STRATEGISCHE ZIELE / KENNZAHLEN / MENGENGERÜSTE</div>
  <div class="legend">
    <span>Steuerbarkeit:</span>
    <span><i class="dot" style="background:#333"></i>direkt steuerbar</span>
    <span><i class="dot" style="background:linear-gradient(90deg,#333 50%,#fff 50%);border:1px solid #333"></i>eingeschränkt steuerbar</span>
    <span><i class="dot" style="border:1px solid #333"></i>nicht steuerbar</span>
    <span>Zielerreichung:</span>
    <span><i class="dot" style="background:#3aa935"></i>nicht gefährdet</span>
    <span><svg width="9" height="8" viewBox="0 0 9 8"><polygon points="4.5,0 9,8 0,8" fill="#f5c400"/></svg>im Toleranzbereich</span>
    <span><i class="dot" style="background:var(--red)"></i>gefährdet</span>
  </div>
  <table class="goals">
    <tr><th rowspan="2" class="corner">Kriminalitätsbekämpfung</th><th colspan="2" style="text-align:center;font-weight:700">Januar - Juni 2019</th><th colspan="2" style="text-align:center;font-weight:700">Ist-Plan Abweichung</th><th style="font-weight:700">2019</th><th rowspan="2" style="text-align:center;font-weight:700">Steuer-<br>barkeit</th><th rowspan="2" style="text-align:center;font-weight:700">Status</th></tr>
    <tr><th>Ist</th><th>Planwert</th><th>abs.</th><th>%</th><th>Planwert</th></tr>
    <tr><td colspan="8" style="border-top:1px solid #999">Leistungen</td></tr>
    <tr><td>300242 Aufklärungsquote [%]</td><td>47,50</td><td>49,00</td><td>-1,50</td><td></td><td>49,00</td><td></td><td rowspan="2" style="text-align:center"><svg width="10" height="9" viewBox="0 0 9 8"><polygon points="4.5,0 9,8 0,8" fill="#f5c400"/></svg></td></tr>
    <tr><td>300596 Anzahl straf. Ermittlungsverf. gesamt [Anz.]</td><td>38.003,000</td><td>44.250,000</td><td>-6.247,000</td><td>-14,12</td><td>88.500,000</td><td></td></tr>
  </table>
  <footer class="footer"><div class="l">Controlling 01-06/19<br>28.09.19</div><div class="pn">41</div><div class="r">07 Inneres</div></footer>
</section>

</body>
</html>
```